Granite Ridge Response Business Card

Side 1: Granite Ridge Response Logo (logo without Maltese cross) with industrial rope rescue related theme. Our company services - TRAINING - Fire Training, Confined Space Rescue Training, Rope Rescue training, Hazmat Training, Incident Command, EMS, Pump Operations Training. Website - graniteridgeresponse.example.
Side 2: Granite Ridge Response Fire Department Logo (logo with Maltese cross) with Firefighter related theme. Company (division) services - FIELD SERVICES - Fire Department, Stand-by Rescue, Safety, EMS, Planning. "Supporting the Emergency Response Community Since 1967"

Add contact information wherever it makes since (Name, Email, Phone).
I would like it to represent the Granite Ridge Response Fire Department Logo as a division not as a separate entity without saying it, possibly by depicting it in the background of Side 2 instead of being a standalone picture like the logo on Side 1.

```html
<!DOCTYPE html>
<html lang="en">
<head>
<meta charset="utf-8">
<title>Granite Ridge Response Business Cards</title>
<link rel="stylesheet" href="https://fonts.googleapis.com/css2?family=Open+Sans:wght@400;600;800&family=Source+Serif+4:wght@700&display=swap">
<style>
  :root {
    --bg: #2b2b2d;
    --card: #ffffff;
    --card-shade: #ececec;
    --red: #e01b24;
    --ink: #222222;
    --grey: #555555;
  }
  * { box-sizing: border-box; margin: 0; padding: 0; }
  html, body { width: 1200px; height: 900px; overflow: hidden; }
  body {
    background: var(--bg);
    font-family: "Open Sans", Arial, sans-serif;
    position: relative;
  }
  .card {
    position: absolute;
    width: 620px;
    height: 354px;
    background: linear-gradient(135deg, var(--card-shade) 0%, var(--card) 55%, var(--card) 100%);
    border-bottom: 12px solid var(--red);
    box-shadow: 0 18px 40px rgba(0,0,0,.55);
    text-align: center;
    color: var(--grey);
  }
  .card--contact { left: 110px; top: 50px; }
  .card--training { left: 470px; top: 486px; }

  .brand {
    display: inline-flex;
    align-items: center;
    gap: 10px;
    font-weight: 800;
    color: var(--red);
    text-transform: uppercase;
    letter-spacing: 2px;
  }
  .brand__mark { width: 14px; height: 14px; background: var(--red); }
  .card--contact .brand { margin-top: 34px; font-size: 22px; }
  .card--training .brand { margin-top: 70px; font-size: 30px; }
  .brand-rule {
    width: 250px; height: 2px; background: var(--red);
    margin: 10px auto 0;
  }

  .person__name {
    font-family: "Source Serif 4", Georgia, serif;
    font-weight: 700;
    color: var(--red);
    font-size: 24px;
    margin-top: 16px;
  }
  .person__title { font-size: 13px; margin-top: 2px; }
  .person__contact {
    font-size: 13px; margin-top: 3px;
    display: flex; justify-content: center; align-items: center; gap: 6px;
  }
  .person__contact svg { width: 13px; height: 13px; fill: var(--red); }
  .sep { color: var(--grey); margin: 0 4px; }

  .services__head {
    display: flex; align-items: center; gap: 10px;
    margin: 16px 34px 6px;
    color: var(--red); font-weight: 800; font-size: 15px;
    text-transform: uppercase; white-space: nowrap;
  }
  .services__head::before, .services__head::after {
    content: ""; flex: 1; height: 1px; background: var(--red);
  }
  .services__list { font-size: 14px; line-height: 1.45; }
  .services__list .bar { color: var(--red); margin: 0 4px; }
  .tagline { color: var(--ink); font-size: 14px; margin-top: 4px; }
  .card--training .services__head { margin-top: 34px; }
</style>
</head>
<body>

<section class="card card--contact">
  <div class="brand"><span class="brand__mark"></span>Granite Ridge Response</div>
  <div class="brand-rule"></div>

  <div class="person">
    <p class="person__name">Dana Whitfield</p>
    <p class="person__title">Safety Specialist II, GRRS / Bayfield Harbor Operations</p>
    <p class="person__contact">
      <svg viewBox="0 0 24 24" aria-hidden="true"><path d="M6.6 10.8a15.1 15.1 0 0 0 6.6 6.6l2.2-2.2a1 1 0 0 1 1-.25 11.4 11.4 0 0 0 3.6.57 1 1 0 0 1 1 1V20a1 1 0 0 1-1 1A17 17 0 0 1 3 4a1 1 0 0 1 1-1h3.5a1 1 0 0 1 1 1c0 1.25.2 2.45.57 3.57a1 1 0 0 1-.25 1z"/></svg>
      (555) 013-0482 <span class="sep">|</span>
      <svg viewBox="0 0 24 24" aria-hidden="true"><path d="M2 5h20v14H2zm2 2v.5l8 5 8-5V7l-8 5z"/></svg>
      dana@graniteridgeresponse.example
    </p>
  </div>

  <h2 class="services__head">Our Services - Field Services</h2>
  <p class="services__list">Fire Department<span class="bar">|</span>Stand-by Rescue<span class="bar">|</span>Safety<span class="bar">|</span>EMS<span class="bar">|</span>Planning</p>
  <p class="tagline">Supporting the Emergency Response Community Since 1967</p>
</section>

<section class="card card--training">
  <div class="brand"><span class="brand__mark"></span>Granite Ridge Response</div>
  <div class="brand-rule"></div>

  <h2 class="services__head">Our Services - Training</h2>
  <p class="services__list">
    Fire Training<span class="bar">|</span>Confined Space Rescue Training<br>
    Rope Rescue training<span class="bar">|</span>Hazmat Training<br>
    Incident Command<span class="bar">|</span>EMS<span class="bar">|</span>Pump Operations Training
  </p>
</section>

</body>
</html>
```